Toronto's Airline, based in Downtown looking for a whole new look and feel.

SkyVarn is looking for a new look in our website. We are an airline based at Corwen Haddle Airfield in Toronto. You can view our current website/services at www.skyvarn.example. We are expanding our services and look forward to a very sleek and modernized website. Please view the different pages on our website, we also need to add several new plane types as we have expanded and the website is not current. Would also be interesting to have a news feed or update feed through a widget which would be easy to use and update. we will also be implementing 2 third party programs called tolvo and quendrix on the website, both are tour based and airline based sales and management functions.

Target Market(s)

Commuters, travel, tourism, dates, general public

Industry/Entity Type

Airline

Coding

Coded - Design and coding required

Number of Pages Required

5+ page

Font styles to use
Other font styles liked:
• Toronto subway font would be nice

Requirements
Must have
• A modern feel, easy to use, our booking function is currently a bit confusing which we will be working on. Content can be taken from our current website www.skyvarn.example
Nice to have
• work with out theme colours of blue and light grey

```html
<!DOCTYPE html>
<html lang="en">
<head>
<meta charset="utf-8">
<title>SkyVarn – Toronto's Airline</title>
<link href="https://fonts.googleapis.com/css2?family=Jost:wght@400;500;600;700&display=swap" rel="stylesheet">
<style>
:root{
  --blue:#2f63b2;
  --blue-deep:#264f91;
  --grey-bg:#efefef;
  --header-bg:#f5f5f5;
  --ink:#1d1d1d;
  --muted:#6b6b6b;
  --footer:#1f2a36;
  --footer-line:#3a4654;
  --footer-text:#a9b3bf;
  --footer-accent:#5d8fd8;
  --white:#ffffff;
  --dark-btn:#222831;
}
*{box-sizing:border-box;margin:0;padding:0}
html,body{width:1200px;height:2908px;overflow:hidden}
body{font-family:"Jost",sans-serif;color:var(--ink);background:var(--white);position:relative}
h1,h2,h3,h4{font-weight:400}

/* header */
.site-header{position:absolute;left:0;top:0;width:1200px;height:80px;background:var(--header-bg)}
.brand{position:absolute;left:142px;top:20px;display:flex;align-items:center;gap:10px;font-size:30px;font-weight:600;color:var(--blue);letter-spacing:1px}
.brand .dot{width:30px;height:30px;border-radius:50%;background:var(--blue)}
.main-nav{position:absolute;left:398px;top:0;height:80px;display:flex}
.main-nav a{display:block;padding:0 13px;line-height:78px;font-size:14px;color:var(--ink);text-decoration:none;position:relative;white-space:nowrap}
.main-nav a.active{color:var(--blue)}
.main-nav a.active::after{content:"";position:absolute;left:0;right:0;bottom:-1px;height:4px;background:var(--blue)}
.btn-book-head{position:absolute;left:972px;top:24px;width:96px;height:32px;border-radius:16px;background:var(--blue);color:#fff;font-size:14px;text-align:center;line-height:32px}

/* hero */
.hero{position:absolute;left:0;top:80px;width:1200px;height:400px;background:linear-gradient(180deg,#8a97a6 0%,#5b6672 45%,#3d4048 70%,#6a6560 100%)}
.hero-title{position:absolute;left:155px;top:122px;color:#fff;font-size:28px;font-weight:600;line-height:1.2}
.hero-sub{position:absolute;left:155px;top:156px;color:#fff;font-size:23px;font-weight:400}
.btn-explore{position:absolute;left:155px;top:211px;width:129px;height:31px;border-radius:16px;background:var(--blue);color:#fff;font-size:14px;text-align:center;line-height:31px}
.hero-dots{position:absolute;left:570px;top:373px;display:flex;gap:8px}
.hero-dots span{width:8px;height:8px;border-radius:50%;background:var(--blue)}
.hero-dots span.on{background:#fff}

/* section heading */
.sec-head{position:absolute;left:92px;display:flex;align-items:center;font-size:19px;font-weight:400;color:var(--ink);white-space:nowrap}
.sec-head::before{content:"";width:48px;height:1px;background:currentColor;opacity:.7;margin-right:14px}
.sec-head b{font-weight:500;color:var(--blue);margin-left:6px}
.sec-head.light{color:#fff}
.sec-head.light b{color:#fff}

/* welcome */
.welcome{position:absolute;left:0;top:480px;width:1200px;height:340px;background:var(--grey-bg)}
.welcome-text{position:absolute;left:155px;top:572px;width:880px;font-size:12.5px;line-height:18px;color:var(--muted)}
.video-frame{position:absolute;left:299px;top:676px;width:602px;height:282px;background:#fff;padding:8px;box-shadow:0 4px 14px rgba(0,0,0,.25)}
.video-still{width:100%;height:100%;background:linear-gradient(120deg,#2d5560 0%,#4d6d74 40%,#1b2328 75%,#363a40 100%);position:relative}
.video-still svg{position:absolute;left:269px;top:111px}

/* services */
.services{position:absolute;left:0;top:820px;width:1200px;height:510px;background:var(--blue)}
.service{position:absolute;top:1062px;width:270px;color:#fff}
.service .icon{height:40px}
.service h3{margin-top:22px;font-size:15px;font-weight:500}
.service .rule{width:48px;height:1px;background:rgba(255,255,255,.6);margin:8px 0 14px}
.service p{font-size:12.5px;line-height:17px}
.btn-read{position:absolute;top:1250px;width:96px;height:32px;border-radius:16px;border:1px solid rgba(255,255,255,.45);color:rgba(255,255,255,.75);font-size:13px;text-align:center;line-height:30px}
.btn-read.solid{background:var(--dark-btn);border-color:var(--dark-btn);color:#fff}

/* tours */
.tabs{position:absolute;left:155px;top:1424px;display:flex}
.tab{height:28px;line-height:28px;font-size:13px}
.tab.on{background:var(--blue);color:#fff;width:103px;text-align:center}
.tab.off{width:172px;color:var(--ink);border-bottom:2px solid var(--blue);padding-left:30px}
.photo{position:absolute}
.pkg{position:absolute;width:380px}
.pkg h4{font-size:15px;font-weight:500;line-height:19px}
.pkg .desc{font-size:12.5px;line-height:17px;color:var(--muted);margin-top:6px}
.pkg .price{font-size:14px;margin-top:10px}
.pkg .price em{font-style:normal;color:var(--blue);font-weight:500}
.btn-pkg{position:absolute;width:112px;height:32px;border-radius:16px;border:1px solid #9fb6da;color:var(--muted);font-size:13px;text-align:center;line-height:30px}
.btn-pkg.solid{background:var(--blue);border-color:var(--blue);color:#fff}

/* newsletter */
.newsletter{position:absolute;left:0;top:2428px;width:1200px;height:80px;background:var(--blue)}
.field{position:absolute;top:2452px;width:252px;height:32px;border-radius:16px;background:#eceef2;font-size:12px;color:#666;padding-left:14px;line-height:32px}
.btn-send{position:absolute;left:931px;top:2452px;width:112px;height:32px;border-radius:16px;background:var(--dark-btn);color:#fff;font-size:13px;display:flex;align-items:center;justify-content:center;gap:8px}

/* footer */
.site-footer{position:absolute;left:0;top:2508px;width:1200px;height:400px;background:var(--footer)}
.foot-brand{position:absolute;left:155px;top:2560px;display:flex;align-items:center;gap:10px;font-size:32px;font-weight:600;color:#fff;letter-spacing:1px}
.foot-brand .dot{width:32px;height:32px;border-radius:50%;background:#fff}
.foot-h{position:absolute;font-size:18px;font-weight:400;color:#fff;white-space:nowrap}
.foot-h b{font-weight:500}
.foot-h.u::after{content:"";display:block;width:40px;height:2px;background:var(--blue);margin-top:10px}
.hours{position:absolute;left:155px;top:2682px;font-size:12.5px;line-height:20px;color:var(--footer-text)}
.hours span{display:inline-block;width:137px;color:var(--footer-accent)}
.socials{position:absolute;left:157px;top:2767px;display:flex;gap:10px;align-items:center;color:#8895a3;font-size:12px}
.socials i{width:12px;height:12px;border-radius:50%;background:#8895a3;display:block}
.quick{position:absolute;left:548px;top:2608px;list-style:none;font-size:12.5px;line-height:29px;color:var(--footer-text)}
.quick li::before{content:"»";margin-right:8px;color:var(--footer-accent)}
.contact{position:absolute;left:764px;top:2596px;font-size:12.5px;color:var(--footer-text);line-height:17px;width:290px}
.contact .lbl{color:var(--footer-accent);margin-top:12px}
.contact .phone{font-size:24px;color:#cfd6de;margin-top:8px;line-height:28px}
.contact .mail{font-size:17px;color:#cfd6de;text-decoration:underline;margin-top:6px}
.foot-rule{position:absolute;left:155px;top:2850px;width:890px;height:1px;background:var(--footer-line)}
.copy{position:absolute;left:155px;top:2868px;font-size:12px;color:#8895a3}
.copy u{color:var(--footer-accent)}
.to-top{position:absolute;left:1031px;top:2862px}
</style>
</head>
<body>

<header class="site-header">
  <div class="brand"><span class="dot"></span>SkyVarn</div>
  <nav class="main-nav">
    <a class="active">Home</a><a>Flights</a><a>Charter &amp; Fleet</a><a>Packages</a><a>Gallery</a><a>Contact</a><a>FAQ</a>
  </nav>
  <div class="btn-book-head">Book Now</div>
</header>

<section class="hero" role="img" aria-label="Small twin-engine aircraft parked on the apron in front of the Toronto skyline">
  <h1 class="hero-title">This Is The Best Way To Enjoy</h1>
  <p class="hero-sub">The CN Tower In Comfort And Style</p>
  <div class="btn-explore">Explore More</div>
  <div class="hero-dots"><span></span><span class="on"></span><span></span><span></span></div>
</section>

<section class="welcome"></section>
<h2 class="sec-head" style="top:522px">Welcome to<b>SkyVarn</b></h2>
<p class="welcome-text">There are many variations of passages of Lorem Ipsum available, but the majority have suffered alteration in some form, by injected humour, or randomised words which don't look even slightly believable. If you are going to use a passage of Lorem Ipsum, you need to be sure there isn't anything embarrassing hidden in the middle of text. All the Lorem Ipsum generators on the Internet tend to repeat predefined chunks as necessary, making this the first true generator on the Internet. It uses a dictionary of over 200 Latin words.</p>

<section class="services"></section>
<div class="video-frame">
  <div class="video-still" role="img" aria-label="Video still of a passenger boarding a private aircraft, greeted by a pilot">
    <svg width="46" height="46" viewBox="0 0 46 46"><circle cx="23" cy="23" r="20" fill="rgba(0,0,0,.25)" stroke="#fff" stroke-width="2.5"/><path d="M18 14 L32 23 L18 32 Z" fill="none" stroke="#fff" stroke-width="2.5" stroke-linejoin="round"/></svg>
  </div>
</div>

<h2 class="sec-head light" style="top:1000px">Our<b>Services</b></h2>

<div class="service" style="left:155px">
  <svg class="icon" width="44" height="40" viewBox="0 0 44 40"><path d="M2 18 L42 2 L30 36 L20 24 Z" fill="#fff"/><path d="M20 24 L42 2" stroke="#2f63b2" stroke-width="2"/></svg>
  <h3>Flights</h3><div class="rule"></div>
  <p>Looking for something new and exciting in toronto? skyvarn, a private airline based at corwen haddle…</p>
</div>
<div class="service" style="left:460px">
  <svg class="icon" width="52" height="40" viewBox="0 0 52 40"><rect x="4" y="6" width="44" height="3" fill="#fff"/><rect x="24" y="8" width="4" height="6" fill="#fff"/><path d="M12 14 H36 Q44 14 44 22 Q44 28 36 28 H20 Q12 28 12 20 Z" fill="#fff"/><rect x="2" y="18" width="12" height="3" fill="#fff"/><rect x="18" y="32" width="24" height="2.5" fill="#fff"/><rect x="22" y="28" width="2" height="5" fill="#fff"/><rect x="36" y="28" width="2" height="5" fill="#fff"/></svg>
  <h3>Private Charter</h3><div class="rule"></div>
  <p>Say goodbye to check-in lines, baggage pick up, and customs. Arrive 15 minutes before departure, the aircraft is on your time…</p>
</div>
<div class="service" style="left:765px">
  <svg class="icon" width="44" height="40" viewBox="0 0 44 40"><rect x="15" y="4" width="14" height="8" rx="2" fill="none" stroke="#fff" stroke-width="3"/><rect x="3" y="11" width="38" height="26" rx="3" fill="#fff"/><rect x="3" y="21" width="38" height="2" fill="#2f63b2"/><rect x="19" y="19" width="6" height="6" fill="#2f63b2"/></svg>
  <h3>Executive Class Terminal</h3><div class="rule"></div>
  <p>Looking for something new and exciting in toronto? skyvarn, a private airline based at corwen haddle…</p>
</div>
<div class="btn-read" style="left:155px">Read More</div>
<div class="btn-read solid" style="left:460px">Read More</div>
<div class="btn-read" style="left:765px">Read More</div>

<h2 class="sec-head" style="top:1373px">Tours &amp;<b>Packages</b></h2>
<div class="tabs"><div class="tab on">Packages</div><div class="tab off">Flights</div></div>

<div class="photo" style="left:155px;top:1485px;width:445px;height:223px;background:linear-gradient(135deg,#f4f4f4 0%,#e9e9e9 55%,#d9d9d9 100%)" role="img" aria-label="Gift card graphic with a red ribbon bow"></div>
<div class="pkg" style="left:650px;top:1497px">
  <h4>Cash Gift Card</h4>
  <p class="desc" style="margin-top:20px">This gift card can be used towards ANY of our packages.</p>
  <p class="price"><em>$200.00</em></p>
</div>
<div class="btn-pkg" style="left:650px;top:1645px">Book Now</div>

<div class="pkg" style="left:155px;top:1736px">
  <h4>Niagara Wine Tasting and Lunch Getaway<br>Flight Package</h4>
  <p class="desc">This package includes sightseeing and return flight from Toronto to Niagara Falls, lunch…</p>
  <p class="price">(Regular Price $449.00) <em>From CAD $299.00</em></p>
</div>
<div class="btn-pkg solid" style="left:155px;top:1868px">Book Now</div>
<div class="photo" style="left:600px;top:1708px;width:445px;height:224px;background:linear-gradient(180deg,#6f7780 0%,#9aa2aa 40%,#3f464d 75%,#2b3036 100%)" role="img" aria-label="Niagara Falls with the city skyline behind and visitors at the railing"></div>

<div class="photo" style="left:155px;top:1932px;width:445px;height:225px;background:linear-gradient(180deg,#9ec0dc 0%,#7b9cb8 35%,#6a7e88 70%,#4b6a85 100%)" role="img" aria-label="Aerial view of downtown Toronto, the CN Tower and the stadium by the lake"></div>
<div class="pkg" style="left:650px;top:1960px">
  <h4>100 KM Aerial Tour of Toronto</h4>
  <p class="desc" style="margin-top:2px">Experience a breathtaking take off right at the foot of the CN Tower and other high-rise buildings. Guests will soar over the Scarborough Bluffs and the Toronto Harbourfront…</p>
  <p class="price">(Regular Price $175.00) <em>From CAD $99.00</em></p>
</div>
<div class="btn-pkg" style="left:650px;top:2090px">Book Now</div>

<div class="pkg" style="left:155px;top:2196px">
  <h4>Private CN Tower Fly By</h4>
  <p class="desc" style="margin-top:2px">The best date experience in Toronto. Enjoy the company of your loved one.</p>
  <p class="price">(Regular Price $190.00) <em>From CAD $109.00</em></p>
</div>
<div class="btn-pkg" style="left:155px;top:2306px">Book Now</div>
<div class="photo" style="left:600px;top:2157px;width:445px;height:223px;background:linear-gradient(180deg,#8fa2b3 0%,#4f6272 40%,#2c3946 75%,#1d2630 100%)" role="img" aria-label="Toronto skyline at dusk seen from above with the CN Tower"></div>

<section class="newsletter"></section>
<h2 class="sec-head light" style="top:2456px">Sign Up<b>Newsletter</b></h2>
<div class="field" style="left:396px">Name:</div>
<div class="field" style="left:663px">Email:</div>
<div class="btn-send"><svg width="13" height="12" viewBox="0 0 13 12"><path d="M0 5 L13 0 L10 12 L6 8 Z" fill="#fff"/></svg>Send</div>

<footer class="site-footer"></footer>
<div class="foot-brand"><span class="dot"></span>SkyVarn</div>
<h3 class="foot-h" style="left:155px;top:2646px">Reservations &amp; Customer Service</h3>
<div class="hours">
  <div><span>Monday – Friday:</span>10:00 am – 5:00 pm</div>
  <div><span>Saturday &amp; Sunday:</span>10:00 am – 4:00 pm</div>
</div>
<h3 class="foot-h" style="left:155px;top:2734px">Follow Us</h3>
<div class="socials"><i></i>/<i></i>/<i></i></div>

<h3 class="foot-h u" style="left:548px;top:2552px">Quick <b>Links</b></h3>
<ul class="quick"><li>Home</li><li>Flights</li><li>Charter &amp; Fleet</li><li>Packages</li><li>Gallery</li><li>Contact</li><li>FAQ</li></ul>

<h3 class="foot-h u" style="left:764px;top:2552px">Contact <b>Us</b></h3>
<div class="contact">
  <div class="lbl">Address:</div>
  <div style="margin-top:8px">Corwen Haddle Airfield Hangar 4,<br>Suite 210 Toronto, Ontario M0X 2B7</div>
  <div class="lbl" style="margin-top:14px">Phone:</div>
  <div class="phone">1-800-555-0142</div>
  <div class="lbl" style="margin-top:10px">Email:</div>
  <div class="mail">info@skyvarn.example</div>
</div>

<div class="foot-rule"></div>
<p class="copy">© 2017 SkyVarn. All rights reserved. &nbsp;<u>Tariffs</u> | <u>Careers</u></p>
<svg class="to-top" width="14" height="24" viewBox="0 0 14 24"><path d="M7 23 V2 M1 8 L7 2 L13 8" fill="none" stroke="#5d8fd8" stroke-width="1.6"/></svg>

</body>
</html>
```